"The Glassblower's Diary" book cover

Book cover for both print paperback and ebook versions of the book.
The book consists of a series of short stories (chapters) depicting various unusual stories of clients of the astrologer and personal experience of the author, a person with a professional duty to forecast future.

It should be neutral to positive. There is no restriction regarding the colors – it can be both B&W and full color.
The design should be original and not include any images which require obtaining a copyright license to use. Symbols in common use and not copyrighted are probably ok. The designer should use appropriate symbols attached in the word file.
Text for the back cover is not yet available, will be ready by the end of the project. The photos of the author for the backside are attached, please choose which you consider the best.
I will need PDF, JPEG, TIFF (all formats both in CMYK and RGB) and the source file. For CMYK, we need files with no color profiles assigned.
Updates

Low design quality

Designs look the same

Target Market(s)

General

Colors

Designer to choose colors to be used in the design.

Requirements
Must have
• Please the project description
Nice to have
Should not have
• Stock images or anything else requiring additional copyright discussions and negotiations.

```html
<!DOCTYPE html>
<html lang="en">
<head>
<meta charset="utf-8">
<title>The Glassblower's Diary – Book Cover</title>
<link rel="stylesheet" href="https://fonts.googleapis.com/css2?family=Oswald:wght@500;600&family=Montserrat:wght@300;400&family=Arimo:wght@400&display=swap">
<style>
  :root {
    --stage: #0a80a8;
    --paper: #ffffff;
    --navy: #14205a;
    --teal: #1a8ab0;
    --ink: #1b1b1b;
    --wash-light: #cfe7f4;
    --wash-mid: #6fa9e0;
    --wash-deep: #3b5fd0;
    --wash-violet: #8a7ee0;
  }
  * { box-sizing: border-box; margin: 0; padding: 0; }
  html, body { width: 1200px; height: 800px; overflow: hidden; }
  body { background: var(--stage); position: relative; font-family: "Arimo", Arial, sans-serif; }

  .cover-wrap {
    position: absolute; left: 65px; top: 20px;
    width: 1070px; height: 760px;
    display: flex; background: var(--paper);
    box-shadow: 0 6px 18px rgba(0,0,0,.25);
  }

  /* Back cover */
  .back {
    position: relative; width: 500px; height: 100%; overflow: hidden;
    background: var(--paper);
  }
  .back-wash {
    position: absolute; inset: 0;
    background:
      radial-gradient(ellipse 60% 45% at 60% 75%, rgba(111,169,224,.75), rgba(111,169,224,0) 70%),
      radial-gradient(ellipse 70% 55% at 50% 45%, rgba(207,231,244,.9), rgba(207,231,244,0) 75%),
      radial-gradient(ellipse 40% 30% at 85% 55%, rgba(59,95,208,.35), rgba(59,95,208,0) 70%);
  }
  .back-content { position: relative; padding: 62px 46px 0 50px; }
  .back-title {
    font-family: "Oswald", "Arial Narrow", sans-serif; font-weight: 600;
    color: var(--teal); font-size: 30px; letter-spacing: .5px;
    text-transform: uppercase; text-align: center; line-height: 1;
  }
  .back-subtitle {
    font-family: "Montserrat", Arial, sans-serif; font-weight: 400;
    font-size: 13px; color: var(--navy); text-align: center; margin-top: 6px;
  }
  .blurb {
    font-size: 10.5px; line-height: 1.35; color: var(--ink); margin-top: 22px;
  }
  .author-block { display: flex; gap: 14px; margin-top: 40px; }
  .author-photo { width: 96px; height: 118px; flex: none; }
  .author-name {
    font-family: "Montserrat", Arial, sans-serif; font-weight: 300;
    font-size: 26px; color: var(--navy); margin-bottom: 6px;
  }
  .author-bio, .author-bio-more { font-size: 10px; line-height: 1.35; color: var(--ink); }
  .author-bio-more { margin-top: 10px; }

  /* Spine */
  .spine {
    position: relative; width: 70px; height: 100%;
    background: linear-gradient(180deg, #f1f5fb 0%, #dfe9f6 35%, #9fc3ec 65%, #c5dcf2 100%);
    display: flex; flex-direction: column; align-items: center;
    justify-content: space-between; padding: 30px 0 34px;
  }
  .spine-title {
    writing-mode: vertical-rl; font-family: "Oswald", "Arial Narrow", sans-serif;
    font-weight: 600; font-size: 24px; color: var(--teal); text-transform: uppercase;
  }
  .spine-author {
    writing-mode: vertical-rl; font-family: "Montserrat", Arial, sans-serif;
    font-weight: 400; font-size: 17px; color: var(--navy);
  }

  /* Front cover */
  .front { position: relative; width: 500px; height: 100%; overflow: hidden; background: var(--paper); }
  .front-art { position: absolute; inset: 0; }
  .front-author {
    position: absolute; top: 48px; left: 0; right: 0; text-align: center;
    font-family: "Montserrat", Arial, sans-serif; font-weight: 300;
    font-size: 40px; color: var(--navy);
  }
  .front-title {
    position: absolute; top: 270px; left: 0; right: 0; text-align: center;
    font-family: "Oswald", "Arial Narrow", sans-serif; font-weight: 600;
    font-size: 70px; line-height: .98; color: var(--paper); text-transform: uppercase;
  }
  .front-subtitle {
    position: absolute; top: 560px; left: 70px; right: 30px;
    font-family: "Montserrat", Arial, sans-serif; font-weight: 400;
    font-size: 24px; line-height: 1.2; color: var(--navy);
  }
  .translator {
    position: absolute; bottom: 60px; left: 100px;
    font-family: "Arimo", Arial, sans-serif; font-size: 17px;
    letter-spacing: 2px; color: var(--ink);
  }
</style>
</head>
<body>
  <div class="cover-wrap">
    <section class="back">
      <div class="back-wash"></div>
      <div class="back-content">
        <h2 class="back-title">The Glassblower's Diary</h2>
        <p class="back-subtitle">Real-life stories on how the stars shapes our lives</p>
        <p class="blurb">Book cover for both print paperback and ebook versions of the book. &lt;br/&gt;The book consists of a series of short stories (chapters) depicting various unusual stories of clients of the astrologer and personal experience of the author, a person with a professional duty to forecast future. &lt;br/&gt;I attached a sketch of the cover. Please consider the sketch as an idea – do not copy it. &lt;br/&gt;The main idea – stars (in form of astrological symbols) falling from the above smear, spread over and form images of basic emotions and – love, grief, happiness, fear, ecstasy, jealousy etc. Images, like patterns in coffee cup reading, should be easily identified by the reader. You can use the watercolor effect for this. The sketch looks a bit mournfully but I do not want the cover to have this impression. It should be neutral to positive. There is no restriction regarding the colors – it can be both B&amp;W and full color. &lt;br/&gt;The design should be original and not include any images which require obtaining a copyright license to use. Symbols in common use and not copyrighted are probably ok. The designer should use appropriate symbols attached in the word file. &lt;br/&gt;Text for the back cover is not yet available, will be ready by the end of the project. The photos of the author for the backside are attached, please choose which you consider the best. &lt;br/&gt;I will need PDF, JPEG, TIFF (all formats both in CMYK and RGB) and the source file. For CMYK, we need files with no color profiles assigned. &lt;br/&gt;</p>
        <div class="author-block">
          <svg class="author-photo" role="img" aria-label="Author portrait photograph" viewBox="0 0 96 118">
            <defs>
              <linearGradient id="portraitTone" x1="0" y1="0" x2="0" y2="1">
                <stop offset="0" stop-color="#e8d9b0"/>
                <stop offset="1" stop-color="#f4eee6"/>
              </linearGradient>
            </defs>
            <rect width="96" height="118" fill="url(#portraitTone)"/>
          </svg>
          <div>
            <h3 class="author-name">Marina Velkova</h3>
            <p class="author-bio">There is no restriction regarding the colors – it can be both B&amp;W and full color. &lt;br/&gt;The design should be original and not include any images which require obtaining a copyright</p>
          </div>
        </div>
        <p class="author-bio-more">license to use. Symbols in common use and not copyrighted are probably ok. The designer should use appropriate symbols attached in the word file. &lt;br/&gt;Text for the back cover is not yet available, will be ready by the end of the project. The photos of the author for the backside are attached, please choose which you consider the best. &lt;br/&gt;I will need PDF, JPEG, TIFF (all formats both in CMYK and RGB) and the source file. For CMYK, we need files with no color profiles assigned. &lt;br/&gt;</p>
      </div>
    </section>

    <section class="spine">
      <span class="spine-title">The Glassblower's Diary</span>
      <span class="spine-author">Marina Velkova</span>
    </section>

    <section class="front">
      <svg class="front-art" role="img" aria-label="Watercolour wash in blue and violet with falling snowflake-like star symbols and silhouettes of people expressing emotions" viewBox="0 0 500 760" preserveAspectRatio="none">
        <defs>
          <radialGradient id="washCore" cx="0.5" cy="0.5" r="0.5">
            <stop offset="0" stop-color="#3b5fd0"/>
            <stop offset="0.45" stop-color="#6f8fe0"/>
            <stop offset="0.75" stop-color="#a7c6ef" stop-opacity=".8"/>
            <stop offset="1" stop-color="#ffffff" stop-opacity="0"/>
          </radialGradient>
          <radialGradient id="washViolet" cx="0.5" cy="0.5" r="0.5">
            <stop offset="0" stop-color="#8a7ee0" stop-opacity=".9"/>
            <stop offset="1" stop-color="#8a7ee0" stop-opacity="0"/>
          </radialGradient>
          <linearGradient id="skyTop" x1="0" y1="0" x2="0" y2="1">
            <stop offset="0" stop-color="#e4edf7"/>
            <stop offset="1" stop-color="#ffffff" stop-opacity="0"/>
          </linearGradient>
        </defs>
        <rect width="500" height="760" fill="#ffffff"/>
        <rect width="500" height="260" fill="url(#skyTop)"/>
        <ellipse cx="250" cy="440" rx="300" ry="330" fill="url(#washCore)"/>
        <ellipse cx="300" cy="260" rx="220" ry="150" fill="url(#washViolet)"/>
      </svg>
      <p class="front-author">Marina Velkova</p>
      <h1 class="front-title">The<br>Glassblower's<br>Diary</h1>
      <p class="front-subtitle">Real-life stories on how<br>the stars shapes our lives</p>
      <p class="translator">Translated by Helen Ashford</p>
    </section>
  </div>
</body>
</html>
```